Building company buisness cards

We are looking for a sharp modern new look for our business cards.We are a New Zealand based company that specialises in house and land packages.We have attached a photo of the current logo and would like to see if it can be improved somehow if needed.We are open to any colours but we have chosen Black and White at this stage. Feel free to change the font and make the logo smarter looking.Play with the colours and see what looks best.We want a card that looks so good know one will want to throw it away!

Target Market(s)

Building profesonals, home buyers

Industry/Entity Type

Building

Contact Information for Business Card

Derek Haskins
0274930268
derekh@stonerange.co.nz

Font styles to use
Serif
Sans Serif

Colors

Designer to choose colors to be used in the design.

Requirements
Must have
• Just the logo on one side and details on the other
• Clean simple looking card
Nice to have
• Round corners and detail like raised or spot UV
• Something that stands out
Should not have
• To title needed, Director etc

```html
<!DOCTYPE html>
<html lang="en">
<head>
<meta charset="utf-8">
<title>Stonerange Business Cards</title>
<link href="https://fonts.googleapis.com/css2?family=Playfair+Display:wght@700&family=Lato:wght@400&display=swap" rel="stylesheet">
<style>
  :root {
    --backdrop: #2e2e2f;
    --card: #1e1e20;
    --card-back: #232325;
    --pattern-tone: #2b2b2e;
    --ink: #f4f3ef;
    --rule: #6a6a6c;
  }
  * { margin: 0; padding: 0; box-sizing: border-box; }
  html, body {
    width: 1200px;
    height: 1108px;
    overflow: hidden;
    background: var(--backdrop);
  }
  .sheet {
    position: relative;
    width: 1200px;
    height: 1108px;
  }
  .card {
    position: absolute;
    top: 234px;
    width: 400px;
    height: 640px;
    border-radius: 26px;
    background: var(--card);
    overflow: hidden;
    color: var(--ink);
  }
  .card--front { left: 150px; }
  .card--back { left: 650px; background: var(--card-back); }

  .brand-name {
    font-family: "Lato", Arial, sans-serif;
    font-weight: 400;
    font-size: 44px;
    line-height: 1;
    letter-spacing: 3px;
    color: var(--ink);
    white-space: nowrap;
  }
  .card--front .brand-name {
    position: absolute;
    left: 36px;
    top: 122px;
  }
  .tagline {
    position: absolute;
    left: 38px;
    top: 176px;
    font-family: "Lato", Arial, sans-serif;
    font-size: 15px;
    letter-spacing: 0.3px;
    color: var(--ink);
  }
  .details {
    position: absolute;
    left: 0;
    right: 0;
    top: 440px;
    text-align: center;
  }
  .details__name {
    font-family: "Playfair Display", Georgia, serif;
    font-weight: 700;
    font-size: 32px;
    color: var(--ink);
  }
  .details__rule {
    width: 200px;
    height: 1px;
    margin: 14px auto;
    background: var(--rule);
  }
  .details__line {
    font-family: "Lato", Arial, sans-serif;
    font-size: 19px;
    line-height: 1.45;
    color: var(--ink);
  }

  .pattern-field {
    position: absolute;
    inset: 0;
    background: linear-gradient(160deg, var(--pattern-tone), var(--card-back));
  }
  .card--back .brand-name {
    position: absolute;
    left: 36px;
    bottom: 82px;
  }
</style>
</head>
<body>
  <main class="sheet">
    <section class="card card--front" aria-label="Card front with contact details">
      <p class="brand-name">Stonerange</p>
      <p class="tagline">Homes shaped around you.</p>
      <div class="details">
        <h1 class="details__name">Derek Haskins</h1>
        <div class="details__rule"></div>
        <p class="details__line">P: 0274930268</p>
        <p class="details__line">E: derekh@stonerange.co.nz</p>
      </div>
    </section>

    <section class="card card--back" aria-label="Card back with brand name">
      <div class="pattern-field" role="img" aria-label="Faint repeating pattern covering the card back"></div>
      <p class="brand-name">Stonerange</p>
    </section>
  </main>
</body>
</html>
```